Bold Vehicle Wrap Design for 2025 Halvorsen Trekmule Cargo Van

We need a full wrap design for our 2025 Halvorsen-Kraft Trekmule 2500 High Roof Cargo Van. This van will be used to represent Brightmark Pro Services, and we want it to stand out with a bold, professional look.

Vehicle Details:
2025 Trekmule 2500
High Roof
144" Wheelbase
Cargo configuration (no windows)

Our current logo is black, white, and gray — but we’re open to more colorful wrap concepts that could even influence a logo recolor.

We want a wrap design that:
Looks bold and professional
Incorporates icons for the services we provide:Plumbing,Handyman, Land Management, Junk and Debris Removal
Incorporates or complements our current logo
Avoids placing critical text or graphics across sliding doors, seams, or complex panel curves
Download all project files (template, logo, reference images):
https://files.quillbarn-share.com/f/7kq2vz9xw4nm18pd5r/BXTLUmQeKsPOtvc3h8rjnZW?key=2pxd9mwq47vbt6c5ls0eyhz3f&s=k8m3vqrt&dl=0

Target Market(s)

ocal residential and commercial customers in need of professional plumbing, handyman, land management, and junk/debris removal services. Homeowners and property managers looking for reliable and skilled service providers. Businesses and contractors who require prompt, professional, and trustworthy support for their facilities and properties. Customers who value quality workmanship and clear branding that conveys professionalism and expertise.

Industry/Entity Type

Local Service Providers specializing in residential and commercial property maintenance

Requirements
Must have
• Incorporate the Brightmark Pro Services logo with flexibility for adding color to complement the wrap. Use bold, professional, and eye-catching colors that stand out on the road. Include icons or visuals representing these key services: Plumbing Handyman Land Management Junk and Debris Removal. Design must fit a 2025 Halvorsen Trekmule 2500 High Roof Cargo Van (144" WB, cargo version with sliding door) — avoid placing important graphics or text over the sliding door seams or complex curves. Use high-contrast text and graphics for maximum readability from a distance. Design should be modern and clean, but bold enough to be memorable. Wrap design must work on all visible sides: driver side, passenger side, rear, and front. Provide final deliverables in Adobe Illustrator (.ai) or Photoshop (.psd) with layered files.
Nice to have
• Mockup images showing the wrap applied to the van template.
Should not have
• Do not place important text, logos, or graphics across the sliding door seam or uneven panel curves — they may get distorted or hidden.No low-contrast text or graphics that make information hard to read from a distance.Do not include any unrelated images or icons that don’t represent Brightmark Pro Services’ core offerings.Do not create a design that looks too similar to competitors or other well-known brands. No fonts that are hard to read or too decorative for a work vehicle.

```html
<!DOCTYPE html>
<html lang="en">
<head>
<meta charset="utf-8">
<title>Brightmark Pro Services – Van Wrap Layout</title>
<link rel="stylesheet" href="https://fonts.googleapis.com/css2?family=Rubik:wght@500;700;800&display=swap">
<style>
  :root{
    --red:#c7261c;
    --red-deep:#8f0d0d;
    --navy:#1c2a5e;
    --slate:#2c4a7c;
    --panel:#ececec;
    --panel-white:#ffffff;
    --trim:#4a4a4a;
    --page:#ffffff;
  }
  *{margin:0;padding:0;box-sizing:border-box}
  html,body{width:884px;height:1200px;overflow:hidden;background:var(--page)}
  .canvas{position:relative;width:884px;height:1200px}
  .wrap-side{position:absolute;left:42px;width:800px;height:280px}
  .wrap-side--driver{top:50px}
  .wrap-side--passenger{top:375px}
  .wrap-front{position:absolute;left:70px;top:700px;width:360px;height:440px}
  .wrap-rear{position:absolute;left:470px;top:700px;width:360px;height:440px}
  .t-service{font-family:"Rubik",sans-serif;font-weight:700;fill:var(--red)}
  .t-phone{font-family:"Rubik",sans-serif;font-weight:800;fill:#fff}
  .t-url{font-family:"Rubik",sans-serif;font-weight:700;fill:#fff}
  .t-brand{font-family:"Rubik",sans-serif;font-weight:800;fill:var(--navy)}
  .t-url-front{font-family:"Rubik",sans-serif;font-weight:700;fill:var(--slate)}
  .t-rear-service{font-family:"Rubik",sans-serif;font-weight:700;fill:#fff}
</style>
</head>
<body>
<main class="canvas">

  <!-- Driver side: cab at left -->
  <svg class="wrap-side wrap-side--driver" viewBox="0 0 800 280" role="group" aria-label="Driver side wrap">
    <rect class="panel-body" x="0" y="0" width="800" height="262" rx="26" fill="var(--panel)"/>
    <polygon class="red-sweep" points="200,262 560,200 730,175 760,40 800,20 800,262" fill="var(--red)"/>
    <polygon class="red-sweep-shade" points="400,262 800,205 800,262" fill="var(--red-deep)"/>
    <rect class="rocker" x="0" y="244" width="800" height="12" fill="var(--trim)"/>
    <line class="accent-navy" x1="320" y1="52" x2="540" y2="10" stroke="var(--navy)" stroke-width="4"/>
    <line class="accent-red" x1="250" y1="150" x2="780" y2="48" stroke="var(--red)" stroke-width="3"/>
    <g class="service-list" transform="translate(300,110) rotate(-11)">
      <circle cx="44" cy="-31" r="5" fill="var(--red)" role="img" aria-label="Junk removal icon"/>
      <text class="t-service" x="54" y="-26" font-size="15">Junk/Debris Removal Services</text>
      <circle cx="0" cy="-5" r="5" fill="var(--red)" role="img" aria-label="Plumbing icon"/>
      <text class="t-service" x="10" y="0" font-size="15">Plumbing</text>
      <circle cx="100" cy="-5" r="5" fill="var(--red)" role="img" aria-label="Handyman icon"/>
      <text class="t-service" x="110" y="0" font-size="15">Handyman</text>
      <circle cx="208" cy="-5" r="5" fill="var(--red)" role="img" aria-label="Land management icon"/>
      <text class="t-service" x="218" y="0" font-size="15">Land Management</text>
    </g>
    <g class="brand-mark" transform="translate(430,180) rotate(-9)">
      <text class="t-brand" x="0" y="0" font-size="48">BRIGHTMARK</text>
      <text class="t-brand" x="4" y="28" font-size="22">PRO SERVICES</text>
    </g>
    <g class="phone-banner" transform="translate(110,220) rotate(-6)">
      <polygon points="0,-18 196,-18 196,-28 220,-2 196,22 0,22" fill="var(--navy)"/>
      <text class="t-phone" x="10" y="9" font-size="20">+1 256-555-0147</text>
    </g>
    <text class="t-url" x="460" y="238" font-size="15" transform="rotate(-9 460 238)">www.brightmarkproservices.net</text>
  </svg>

  <!-- Passenger side: cab at right -->
  <svg class="wrap-side wrap-side--passenger" viewBox="0 0 800 280" role="group" aria-label="Passenger side wrap">
    <rect class="panel-body" x="0" y="0" width="800" height="262" rx="26" fill="var(--panel)"/>
    <polygon class="red-sweep" points="600,262 240,200 70,175 40,40 0,20 0,262" fill="var(--red)"/>
    <polygon class="red-sweep-shade" points="400,262 0,205 0,262" fill="var(--red-deep)"/>
    <rect class="rocker" x="0" y="244" width="800" height="12" fill="var(--trim)"/>
    <line class="accent-navy" x1="320" y1="18" x2="540" y2="52" stroke="var(--navy)" stroke-width="4"/>
    <line class="accent-red" x1="120" y1="70" x2="640" y2="152" stroke="var(--red)" stroke-width="3"/>
    <g class="service-list" transform="translate(250,40) rotate(9)">
      <circle cx="0" cy="-5" r="5" fill="var(--red)" role="img" aria-label="Plumbing icon"/>
      <text class="t-service" x="10" y="0" font-size="15">Plumbing</text>
      <circle cx="120" cy="-5" r="5" fill="var(--red)" role="img" aria-label="Junk removal icon"/>
      <text class="t-service" x="130" y="0" font-size="15">Junk/Debris Removal Services</text>
      <circle cx="120" cy="19" r="5" fill="var(--red)" role="img" aria-label="Handyman icon"/>
      <text class="t-service" x="130" y="24" font-size="15">Handyman</text>
      <circle cx="228" cy="19" r="5" fill="var(--red)" role="img" aria-label="Land management icon"/>
      <text class="t-service" x="238" y="24" font-size="15">Land Management</text>
    </g>
    <g class="brand-mark" transform="translate(80,118) rotate(8)">
      <text class="t-brand" x="0" y="0" font-size="48">BRIGHTMARK</text>
      <text class="t-brand" x="4" y="28" font-size="22">PRO SERVICES</text>
    </g>
    <g class="phone-banner" transform="translate(500,172) rotate(6)">
      <polygon points="0,-30 10,-20 210,-20 210,20 12,20 0,-30" fill="var(--navy)"/>
      <text class="t-phone" x="16" y="8" font-size="20">+1 256-555-0147</text>
    </g>
    <text class="t-url" x="140" y="196" font-size="15" transform="rotate(8 140 196)">www.brightmarkproservices.net</text>
  </svg>

  <!-- Front -->
  <svg class="wrap-front" viewBox="0 0 360 440" role="group" aria-label="Front wrap">
    <rect x="0" y="0" width="360" height="440" rx="28" fill="var(--panel-white)" stroke="#d8d8d8"/>
    <text class="t-url-front" x="180" y="60" font-size="16" text-anchor="middle">www.brightmarkproservices.net</text>
    <g class="brand-mark" transform="translate(180,250)">
      <text class="t-brand" x="0" y="0" font-size="34" text-anchor="middle">BRIGHTMARK</text>
      <text class="t-brand" x="0" y="24" font-size="16" text-anchor="middle">PRO SERVICES</text>
    </g>
  </svg>

  <!-- Rear -->
  <svg class="wrap-rear" viewBox="0 0 360 440" role="group" aria-label="Rear wrap">
    <rect x="0" y="0" width="360" height="440" rx="28" fill="var(--red)"/>
    <rect class="rear-white-field" x="24" y="14" width="312" height="200" rx="20" fill="var(--panel-white)"/>
    <g class="brand-mark" transform="translate(180,110)">
      <text class="t-brand" x="0" y="0" font-size="40" text-anchor="middle">BRIGHTMARK</text>
      <text class="t-brand" x="0" y="28" font-size="18" text-anchor="middle">PRO SERVICES</text>
    </g>
    <rect class="phone-tab" x="70" y="186" width="220" height="40" rx="10" fill="var(--red)"/>
    <text class="t-phone" x="180" y="214" font-size="22" text-anchor="middle">+1 256-555-0147</text>
    <path class="service-band" d="M14,252 H160 Q190,252 200,290 H346 V340 H160 Q140,340 130,320 H14 Z" fill="var(--slate)"/>
    <circle cx="32" cy="270" r="6" fill="#fff" role="img" aria-label="Plumbing icon"/>
    <text class="t-rear-service" x="44" y="276" font-size="17">Plumbing</text>
    <circle cx="32" cy="302" r="6" fill="#fff" role="img" aria-label="Handyman icon"/>
    <text class="t-rear-service" x="44" y="308" font-size="17">Handyman</text>
    <circle cx="196" cy="306" r="4" fill="#fff" role="img" aria-label="Land management icon"/>
    <text class="t-rear-service" x="206" y="310" font-size="10.5">Land management</text>
    <circle cx="196" cy="324" r="4" fill="#fff" role="img" aria-label="Junk removal icon"/>
    <text class="t-rear-service" x="206" y="328" font-size="10.5">Junk removal services</text>
    <text class="t-url" x="340" y="370" font-size="10" text-anchor="end">www.brightmarkproservices.net</text>
  </svg>

</main>
</body>
</html>
```